Commercial HVAC and Refrigeration Business cards

Frost-Haven Company is looking for flashy new business cards! We design, install, service and maintain commercial refrigeration, air conditioning, heating and refrigeration equipment. Our colors are blue and white. I'm open to single and double sided designs. Each employee will have their own business card. I've attached a copy of our current logo.

Our website, office and cell phone (cell phone is optional), email address should be clearly legible. "24 Hour Service" and the services we offer are; Sales, Service, Design, Installation, Maintenance. Refrigeration, Heating, Air Conditioning, Ice Machines. Does not have to be in any order.

Target Market(s)

Commercial; Restaurants, hotels, bars, breweries etc.

Industry/Entity Type

Hvac

Contact Information for Business Card

Name; Job Title, Phone Number, Email Address. www.frost-haven-example.com 24 Hour Service. We provide - Sales, Design, Installation, Service, Maintenance. We service - Refrigeration, Heating, Air Conditioning, Ice Machines

Font styles to use
Other font styles liked:
• Be creative

Colors
0255a3
ffffff

Requirements
Must have
• Professional appearance and appeal to commercial clients in the food-service and hospitality industry. Must be clearly legible and easy to understand.
Nice to have
• We want to sell maintenance agreements, perhaps we can use the back of the card to tie into a webpage about our maintenance agreements.
Should not have
• Cartoons or unprofessional. Nothing too edgy.

```html
<!DOCTYPE html>
<html lang="en">
<head>
<meta charset="utf-8">
<title>Frost-Haven Company – Business Cards</title>
<link href="https://fonts.googleapis.com/css2?family=Open+Sans:wght@400;600;700&display=swap" rel="stylesheet">
<style>
  :root {
    --brand-blue: #0255a3;
    --blue-light: #4f7fba;
    --blue-deep: #0c2a66;
    --ink-blue: #1d3f82;
    --white: #ffffff;
    --stage: #e9ebef;
    --card-shadow: rgba(10, 25, 60, 0.25);
  }
  * { box-sizing: border-box; margin: 0; padding: 0; }
  html, body { width: 1200px; height: 913px; overflow: hidden; }
  body {
    background: var(--stage);
    font-family: "Open Sans", Arial, sans-serif;
    position: relative;
  }
  .card {
    position: absolute;
    left: 300px;
    width: 600px;
    height: 343px;
    box-shadow: 0 8px 24px var(--card-shadow);
    overflow: hidden;
  }
  /* Front */
  .card--front {
    top: 90px;
    background: linear-gradient(135deg, var(--blue-light) 0%, var(--brand-blue) 45%, var(--blue-deep) 100%);
    color: var(--white);
  }
  .front__brand {
    position: absolute;
    left: 36px;
    top: 210px;
    font-size: 24px;
    font-weight: 700;
    letter-spacing: 0.3px;
    color: var(--white);
    white-space: nowrap;
  }
  .front__rule {
    position: absolute;
    left: 0;
    right: 150px;
    top: 252px;
    height: 1px;
    background: var(--white);
    opacity: 0.8;
  }
  .front__tab {
    position: absolute;
    right: 0;
    top: 38px;
    width: 18px;
    height: 36px;
    background: var(--white);
  }
  .front__contact {
    position: absolute;
    right: 30px;
    top: 38px;
    text-align: right;
  }
  .person__name {
    font-size: 24px;
    font-weight: 700;
    line-height: 1.2;
  }
  .person__title {
    display: inline-block;
    font-size: 13px;
    padding-left: 60px;
    border-top: 1px solid var(--white);
    margin-top: 2px;
    margin-bottom: 12px;
  }
  .contact__line {
    display: flex;
    justify-content: flex-end;
    align-items: center;
    gap: 10px;
    font-size: 13px;
    line-height: 21px;
    white-space: nowrap;
  }
  .contact__icon { width: 12px; height: 12px; flex: none; }
  /* Back */
  .card--back {
    top: 480px;
    background: var(--white);
    color: var(--ink-blue);
  }
  .back__brand {
    position: absolute;
    right: 60px;
    top: 70px;
    font-size: 36px;
    font-weight: 700;
    color: var(--brand-blue);
    white-space: nowrap;
  }
  .back__services {
    position: absolute;
    left: 40px;
    bottom: 40px;
    font-size: 14px;
    font-weight: 600;
    line-height: 1.35;
  }
  .services__headline {
    font-size: 17px;
    font-weight: 700;
    margin-bottom: 2px;
  }
  .services__label { font-weight: 700; }
</style>
</head>
<body>

<section class="card card--front" aria-label="Business card front">
  <div class="front__brand">Frost-Haven Company</div>
  <div class="front__rule"></div>
  <div class="front__tab"></div>
  <div class="front__contact">
    <div class="person__name">Mark Delaney</div>
    <div class="person__title">President</div>
    <div class="contact__line">012 555 0190
      <svg class="contact__icon" viewBox="0 0 12 12"><rect x="3" y="0.5" width="6" height="11" rx="1" fill="none" stroke="#fff"/><circle cx="6" cy="9.5" r="0.8" fill="#fff"/></svg>
    </div>
    <div class="contact__line">866-555-0148 (Toll Free)
      <svg class="contact__icon" viewBox="0 0 12 12"><path d="M1 4 Q6 0 11 4 L9 5.5 L8 4 L4 4 L3 5.5 Z" fill="#fff"/><rect x="2.5" y="6" width="7" height="5" rx="1" fill="#fff"/></svg>
    </div>
    <div class="contact__line">mdelaney@frost-haven-example.com
      <svg class="contact__icon" viewBox="0 0 12 12"><rect x="0.5" y="2.5" width="11" height="7" fill="none" stroke="#fff"/><path d="M0.5 2.5 L6 6.5 L11.5 2.5" fill="none" stroke="#fff"/></svg>
    </div>
    <div class="contact__line">www.frost-haven-example.com
      <svg class="contact__icon" viewBox="0 0 12 12"><circle cx="6" cy="6" r="5.5" fill="none" stroke="#fff"/><ellipse cx="6" cy="6" rx="2.3" ry="5.5" fill="none" stroke="#fff"/><line x1="0.5" y1="6" x2="11.5" y2="6" stroke="#fff"/></svg>
    </div>
  </div>
</section>

<section class="card card--back" aria-label="Business card back">
  <div class="back__brand">Frost-Haven Company</div>
  <div class="back__services">
    <div class="services__headline">24 HOUR SERVICE</div>
    <div class="services__label">We provide:</div>
    <div>Sales, Design, Installation, Service, Maintenance.</div>
    <div class="services__label">We service:</div>
    <div>Refrigeration, Heating, Air Conditioning, Ice Machines</div>
  </div>
</section>

</body>
</html>
```